Rebrand of 3 bottle labels for nail polish brand

The task is to make a rebranding of our current gel nail polish bottle design. We have become one of the leading european nail polish brand, so we want to improve the quality of the label design to a more scandinavian and minimalistic bottle design, which stille has to be recognisable and unique.

We have attached a more detailed description of the rebranding instructions for our gel polish bottles called "bottle task".
Updates

The Labels should not be just Black and White as stated. But should be mainly Black and White and then some of our color as explained in the uploaded file.

Target Market(s)

Girls and women age 18-55 Northern Europe

Industry/Entity Type

Cosmetic/ Nail Gel Polish

Colors

Designer to choose only greyscale colors for use in the design.

Requirements
Must have
• See attched design instruction
Nice to have
• Moderne, Minimalist, Recognizable and Unique look
Should not have
• Too many elements, too busy design

```html
<!DOCTYPE html>
<html lang="en">
<head>
<meta charset="utf-8">
<title>Velmora Color Coat – label 21</title>
<link href="https://fonts.googleapis.com/css2?family=Cinzel:wght@500&family=Montserrat:wght@300;400&family=Roboto+Condensed:wght@300;400;500&display=swap" rel="stylesheet">
<style>
  :root {
    --page: #ffffff;
    --label-black: #222222;
    --ink-white: #ffffff;
    --ink-soft: #e6e6e6;
    --taupe: #bc9e94;
    --number-black: #1c1c1c;
    --faint: #3a3a3a;
    --hazard-red: #d8202a;
  }
  * { margin: 0; padding: 0; box-sizing: border-box; }
  html, body { width: 1200px; height: 1200px; overflow: hidden; background: var(--page); }
  .canvas { position: relative; width: 1200px; height: 1200px; }

  .label {
    position: absolute; left: 30px; top: 448px;
    width: 1140px; height: 304px;
    background: var(--label-black); color: var(--ink-white);
    overflow: hidden;
  }
  .abs { position: absolute; }
  .vertical { writing-mode: vertical-rl; transform: rotate(180deg); white-space: nowrap; }

  .volume {
    left: 24px; top: 94px; height: 126px;
    font-family: "Montserrat", sans-serif; font-weight: 400; font-size: 19px;
    display: flex; align-items: center; justify-content: center;
  }

  .front { left: 140px; top: 0; width: 242px; height: 304px; text-align: center; }
  .brand-name {
    font-family: "Montserrat", sans-serif; font-weight: 300;
    font-size: 40px; letter-spacing: 1px;
  }
  .front .brand-name { position: absolute; top: 42px; left: 0; width: 100%; }
  .product-title {
    position: absolute; top: 132px; left: 0; width: 100%;
    font-family: "Cinzel", serif; font-weight: 500; font-size: 29px; letter-spacing: 0.5px;
  }
  .product-sub {
    position: absolute; top: 174px; left: 0; width: 100%;
    font-family: "Montserrat", sans-serif; font-weight: 300; font-size: 13px; letter-spacing: 4px;
    color: var(--ink-soft);
  }
  .dots { position: absolute; top: 205px; left: 0; width: 100%; font-size: 20px; letter-spacing: 2px; line-height: 1; font-family: "Montserrat", sans-serif; }
  .leaf-mark { position: absolute; left: 26px; top: 190px; width: 88px; height: 82px; border-radius: 50% 50% 44% 44%; background: var(--faint); opacity: 0.45; }
  .vegan-script { position: absolute; left: 48px; top: 244px; width: 154px; height: 30px; border-radius: 4px; background: #4a4a4a; }

  .shade-band { left: 400px; top: 0; width: 57px; height: 304px; background: var(--taupe); }
  .shade-name {
    left: 408px; top: 30px; height: 190px;
    font-family: "Roboto Condensed", sans-serif; font-weight: 400; font-size: 30px;
    color: var(--number-black); display: flex; align-items: center; justify-content: center;
  }
  .shade-number {
    left: 403px; top: 250px; width: 51px; height: 52px; background: var(--number-black);
    font-family: "Roboto Condensed", sans-serif; font-weight: 500; font-size: 32px;
    display: flex; align-items: center; justify-content: center;
  }

  .side-brand {
    left: 488px; top: 16px; height: 270px;
    font-size: 66px; line-height: 1;
    display: flex; align-items: center; justify-content: center;
  }
  .origin {
    left: 576px; top: 80px; height: 150px;
    font-family: "Roboto Condensed", sans-serif; font-weight: 400; font-size: 17px;
    display: flex; align-items: center; justify-content: center;
  }

  .info {
    left: 628px; top: 17px; width: 326px;
    font-family: "Roboto Condensed", sans-serif; font-weight: 300; font-size: 13px; line-height: 15.3px;
    text-align: justify; color: var(--ink-soft);
  }
  .info p { margin-bottom: 5px; }
  .info strong { font-weight: 500; color: var(--ink-white); }

  .icons { left: 978px; top: 18px; width: 80px; height: 272px; }
  .address {
    left: 1082px; top: 16px; height: 270px;
    font-family: "Roboto Condensed", sans-serif; font-weight: 400; font-size: 13px; line-height: 17px;
    display: flex; align-items: center; justify-content: center; text-align: center;
  }
</style>
</head>
<body>
<div class="canvas">
  <section class="label" aria-label="Velmora Color Coat bottle label, shade 21">
    <div class="abs volume vertical">15ml ℮ 0.5oz</div>

    <div class="abs front">
      <div class="leaf-mark" role="img" aria-label="Faint leaf emblem"></div>
      <div class="brand-name">velmora</div>
      <div class="product-title">COLOR COAT</div>
      <div class="product-sub">SOAK OFF UV/LED</div>
      <div class="dots">•••</div>
      <div class="vegan-script" role="img" aria-label="Hand lettered 'Vegan Formula'"></div>
    </div>

    <div class="abs shade-band"></div>
    <div class="abs shade-name vertical">COLOR NAME</div>
    <div class="abs shade-number">21</div>

    <div class="abs side-brand vertical brand-name">velmora</div>
    <div class="abs origin vertical">Made in Germany</div>

    <div class="abs info">
      <p><strong>DIRECTIONS FOR USE (ENG):</strong> Velmora Color Coat must be applied in thin layers and cured in one of our Velmora Lamps.</p>
      <p><strong>ANVENDELSE (DK):</strong> Velmora Farver skal påføres i tynde lag og hærdes i en af vores Velmora Lamper.</p>
      <p><strong>CAUTION (ENG):</strong> Keep out of reach of children. Discontinue use if irritation occurs. Avoid direct sunlight or extreme exposure to LED or UV Light.</p>
      <p><strong>ADVARSEL (DK):</strong> Opbevar utilgængeligt for børn. Stop din behandling, hvis produktet forudsager irritation. Undgå direkte sollys eller udsættelse for LED eller UV.</p>
      <p><strong>INGREDIENTS:</strong> Acrylates Copolymer, Acrylated Aliphatic Urethane, Cellulose Acetate Butanoate, Dimethicone, Ceresine, wax, Pigment Red, Carbon Black, Titanium dioxide, CI 77891</p>
    </div>

    <svg class="abs icons" viewBox="0 0 80 272" aria-label="Safety and recycling icons">
      <!-- hazard -->
      <rect x="23" y="9" width="34" height="34" transform="rotate(45 40 26)" fill="var(--ink-white)" stroke="var(--hazard-red)" stroke-width="4"/>
      <rect x="37.5" y="14" width="5" height="15" rx="2" fill="#000"/>
      <circle cx="40" cy="35" r="3" fill="#000"/>
      <!-- period after opening jar -->
      <g fill="none" stroke="var(--ink-white)" stroke-width="1.6">
        <path d="M16 90 L62 72 L64 77 L18 95 Z"/>
        <path d="M18 100 L62 100 L60 124 Q40 129 20 124 Z"/>
        <ellipse cx="40" cy="100" rx="22" ry="4"/>
      </g>
      <text x="40" y="119" text-anchor="middle" font-family="Roboto Condensed, sans-serif" font-size="10" fill="var(--ink-white)">24M</text>
      <!-- recycle -->
      <g fill="none" stroke="var(--ink-white)" stroke-width="5" stroke-linejoin="round">
        <path d="M32 150 L40 137 L48 150"/>
        <path d="M55 160 L60 172 L45 172"/>
        <path d="M34 172 L20 172 L26 160"/>
      </g>
      <g fill="var(--ink-white)">
        <path d="M45 146 L53 149 L52 140 Z"/>
        <path d="M46 166 L40 172 L46 178 Z"/>
        <path d="M22 156 L30 156 L27 164 Z"/>
      </g>
      <!-- shake icon -->
      <rect x="8" y="206" width="62" height="58" rx="6" fill="#3c3c3c" role="img" aria-label="Shake before use pictogram"/>
    </svg>

    <div class="abs address vertical">Nordlys Partners A/S - Strandvejen 41C<br>2900 Hellerup, Denmark</div>
  </section>
</div>
</body>
</html>
```